DL flyer for mobile auto electrician

We need a DL flyer designed for distribution outlining the services provided by our mobile auto electrical business. Logo and text will be provided. The flyer will be distributed with the local newspaper and other advertising materials so we need something that will stand out from the crowd!

Our business is 'Brightpath Road Electrics' and our colours are blue and red which you will be able to see through the logo.

Industry/Entity Type

Electrician

```html
<!DOCTYPE html>
<html lang="en">
<head>
<meta charset="utf-8">
<title>Brightpath Road Electrics – DL Flyer</title>
<link rel="stylesheet" href="https://fonts.googleapis.com/css2?family=Exo+2:ital,wght@0,800;1,800&family=Roboto+Condensed:ital,wght@1,700&family=Open+Sans:ital,wght@1,500;1,700&display=swap">
<style>
  :root {
    --page-bg: #ece8e2;
    --white: #ffffff;
    --brand-blue: #1b8fd6;
    --blue-deep: #0a7cc4;
    --blue-light: #2aa3e6;
    --red-deep: #c9161d;
    --red: #e0301e;
    --orange: #f26a21;
    --silver-light: #e9ebee;
    --silver-dark: #8d939a;
    --car-light: #c4c8cd;
    --car-dark: #6f757c;
  }
  * { box-sizing: border-box; margin: 0; padding: 0; }
  html, body { width: 800px; height: 1200px; overflow: hidden; }
  body { background: var(--page-bg); position: relative; }

  .flyer {
    position: absolute; left: 150px; top: 60px;
    width: 520px; height: 1100px;
    background: var(--white);
    overflow: hidden;
    box-shadow: 0 2px 10px rgba(0,0,0,0.12);
  }

  .header {
    position: absolute; left: 0; top: 0; width: 100%; height: 160px;
    background: var(--white);
    display: flex; align-items: center; justify-content: center; gap: 14px;
    padding-bottom: 10px;
  }
  .brand-dot {
    width: 32px; height: 32px; border-radius: 50%;
    background: var(--brand-blue);
  }
  .brand-name {
    font-family: "Exo 2", sans-serif; font-weight: 800;
    font-size: 28px; color: var(--brand-blue);
  }

  .silver-band {
    position: absolute; left: 0; top: 148px; width: 100%; height: 36px;
    background: linear-gradient(90deg, var(--silver-dark), var(--silver-light) 45%, var(--silver-dark));
    clip-path: polygon(0 60%, 100% 0, 100% 100%, 0 100%);
  }

  .services {
    position: absolute; left: 0; top: 178px; width: 100%; height: 640px;
    background: radial-gradient(circle at 55% 55%, var(--orange) 0%, var(--red) 55%, var(--red-deep) 100%);
  }
  .headline {
    position: absolute; left: 0; top: 42px; width: 100%;
    text-align: center; color: var(--white);
    font-family: "Exo 2", sans-serif; font-style: italic; font-weight: 800;
    font-size: 30px; line-height: 40px; text-transform: uppercase;
  }
  .service-list {
    position: absolute; left: 38px; top: 219px; list-style: none;
  }
  .service-list li {
    display: flex; align-items: center; height: 46px;
    color: var(--white); text-transform: uppercase;
    font-family: "Roboto Condensed", sans-serif; font-style: italic; font-weight: 700;
    font-size: 24px;
  }
  .service-list svg { width: 40px; height: 36px; margin-right: 8px; flex: none; }

  .contact {
    position: absolute; left: 0; top: 815px; width: 100%; height: 285px;
    background: linear-gradient(180deg, var(--blue-light), var(--blue-deep));
  }

  .vehicle-photo {
    position: absolute; left: 15px; top: 690px; width: 472px; height: 145px;
    border-radius: 70px 100px 28px 28px / 60px 70px 28px 28px;
    background: linear-gradient(180deg, var(--car-light), var(--car-dark));
    box-shadow: 0 14px 14px -8px rgba(0,0,0,0.45);
  }

  .contact-tab {
    position: absolute; left: 0; top: 865px; width: 178px; height: 34px;
    background: var(--white);
    clip-path: polygon(0 0, 100% 0, 88% 100%, 0 100%);
    padding-left: 18px;
    font-family: "Open Sans", sans-serif; font-style: italic; font-weight: 700;
    font-size: 19px; line-height: 34px; color: var(--brand-blue);
  }
  .contact-details {
    position: absolute; left: 48px; top: 910px; color: var(--white);
    font-family: "Open Sans", sans-serif; font-style: italic; font-weight: 500;
    font-size: 20px; line-height: 35px;
  }
  .contact-name { font-weight: 700; font-size: 22px; }
  .contact-email { font-size: 18px; }
</style>
</head>
<body>
  <main class="flyer">
    <header class="header">
      <span class="brand-dot"></span>
      <span class="brand-name">Brightpath Road Electrics</span>
    </header>

    <section class="services">
      <h1 class="headline">Experienced mobile auto<br>electrician servicing<br>all residential, commercial<br>and heavy duty vehicles.</h1>
      <ul class="service-list">
        <li><svg viewBox="0 0 40 36"><path d="M2 20 L9 15 L15 25 L36 2 L39 5 L15 34 Z" fill="#fff"/></svg>Boats</li>
        <li><svg viewBox="0 0 40 36"><path d="M2 20 L9 15 L15 25 L36 2 L39 5 L15 34 Z" fill="#fff"/></svg>Air Conditioning</li>
        <li><svg viewBox="0 0 40 36"><path d="M2 20 L9 15 L15 25 L36 2 L39 5 L15 34 Z" fill="#fff"/></svg>Camper Trailers</li>
        <li><svg viewBox="0 0 40 36"><path d="M2 20 L9 15 L15 25 L36 2 L39 5 L15 34 Z" fill="#fff"/></svg>Mine Site Fit Outs</li>
        <li><svg viewBox="0 0 40 36"><path d="M2 20 L9 15 L15 25 L36 2 L39 5 L15 34 Z" fill="#fff"/></svg>Spotlights &amp; Dual Battery Systems</li>
        <li><svg viewBox="0 0 40 36"><path d="M2 20 L9 15 L15 25 L36 2 L39 5 L15 34 Z" fill="#fff"/></svg>All Aspects of Diagnosis &amp; Repairs</li>
      </ul>
    </section>

    <div class="silver-band"></div>

    <section class="contact"></section>

    <div class="vehicle-photo" role="img" aria-label="Photo of a silver sedan shown side-on"></div>

    <div class="contact-tab">Contact us:</div>
    <address class="contact-details">
      <div class="contact-name">Miles Hartley</div>
      <div>P. 0412 555 018</div>
      <div class="contact-email">E. mhartley@brightpath.com.au</div>
      <div>ABN 12 345 678 901</div>
      <div>AU10482</div>
    </address>
  </main>
</body>
</html>
```